Zesty Closers Banner for website:

We are doing up a banner for a Zesty Closers Website on this wordpress theme: http://demo.quillframe.net/compact/
Our theme for Zesty closers is that - We exist to create enormously successful salespeople and savvy business people to take you them to the top!
Our logo is attached below and uses Trajan Font. You can either incorporate it or not (we don't mind either way as you see with the example banners they don't incorporate their logos at all).
We want the banner split into two sections, biggest part at the top with picture and this will also have writing in it which guides people to our newsletter (our main aim is to get people from the banner first look to sign up to our newsletter). The second part which is smaller will have the newsletter area/sign up.
Some favourite banners for ideas are:
- http://www.janetbrimwick.com/ - this this as what we want is similar to above, want to split ours like this to funnel people into our newsletter.
- www.bloomandbranchstudio.com.au - we like this one as it has a picture but also writing
- http://corinnevaldemar.com/ - quite like this banner as it comes across to a very similar target market and looks professional
Was thinking the words something around: Believe you can be the best....? Open to other ideas.
I can send some photos if you like, but thought you might like to see what you would want to do before any photos went out. We have attached logo below and a social media arrow slide that we thought looked quite cool but it would have to be adjusted to the words Sales in the circle and words like customers, profit, money, margin, products, services in arrows. Not a must have but just a thought??? You guys are the gurus you normally come up with something very cool.
Our target market is Corporate sales people and teams, businesses (both new and existing to improve sales) and new business owners starting up businesses (especially women on how to sell) but really anyone wanting to know how to sell!!!
- Two sections, one part for picture to sell the idea to sign up to our newsletter, the other part for newsletter sign up

```html
<!DOCTYPE html>
<html lang="en">
<head>
<meta charset="utf-8">
<title>Zesty Closers — Newsletter Banner</title>
<link rel="stylesheet" href="https://fonts.googleapis.com/css2?family=Cinzel:wght@700;900&family=Arimo:ital,wght@0,400;0,700;1,700&display=swap">
<style>
  :root {
    --cyan: #1fb8ee;
    --cyan-soft: #9fe0f8;
    --white: #ffffff;
    --panel-line: #c9ced6;
    --headline: #0b0ba8;
    --headline-shadow: rgba(20, 20, 60, 0.55);
    --band-edge: #2b2bd6;
    --band-top: #c8e4fb;
    --band-mid: #7fb6ea;
    --band-low: #2c3fa8;
    --band-text: #eef3ff;
    --field: #e4e4e8;
    --field-text: #8a8a92;
    --photo-a: #b9a48c;
    --photo-b: #d9cfc4;
  }
  * { margin: 0; padding: 0; box-sizing: border-box; }
  html, body { width: 1200px; height: 489px; overflow: hidden; background: var(--white); }
  .banner {
    position: relative; width: 1200px; height: 489px; overflow: hidden;
    background: radial-gradient(ellipse 620px 520px at 0 60px, var(--cyan) 0%, var(--cyan-soft) 45%, var(--white) 80%);
  }
  .hero-panel {
    position: absolute; left: 29px; top: 26px; width: 1139px; height: 360px;
    border: 2px solid var(--panel-line); border-radius: 14px;
    background: linear-gradient(90deg, rgba(255,255,255,0) 0%, rgba(255,255,255,0.7) 35%, var(--white) 55%);
  }
  .headline {
    position: absolute; left: 524px; top: 98px; width: 660px;
    font-family: "Cinzel", serif; font-weight: 900; color: var(--headline);
    font-size: 57px; line-height: 60px; letter-spacing: 1px;
    text-shadow: 4px 4px 4px var(--headline-shadow);
  }
  .headline .big { font-size: 64px; }
  .signup-band {
    position: absolute; left: 0; top: 373px; width: 1200px; height: 116px;
    border: 3px solid var(--band-edge); border-right: none; border-bottom: none;
    border-radius: 50px 0 0 0;
    background: linear-gradient(180deg, var(--band-top) 0%, var(--band-mid) 45%, var(--band-low) 100%);
  }
  .signup-pitch {
    position: absolute; left: 18px; top: 52px; white-space: nowrap;
    font-family: "Arimo", sans-serif; font-size: 22px; color: var(--band-text);
  }
  .signup-pitch em { font-style: italic; font-weight: 700; }
  .signup-pitch strong { font-weight: 700; }
  .signup-field {
    position: absolute; top: 42px; height: 31px; background: var(--field);
    font-family: "Arimo", sans-serif; font-size: 19px; color: var(--field-text);
    padding: 4px 0 0 23px;
  }
  .signup-field--name { left: 477px; width: 270px; }
  .signup-field--email { left: 768px; width: 264px; }
  .signup-go {
    position: absolute; left: 1048px; top: 22px;
    font-family: "Arimo", sans-serif; font-weight: 700; font-size: 64px; line-height: 64px;
    color: var(--white);
  }
  .portrait {
    position: absolute; border-radius: 50%; border: 5px solid var(--white);
    background: radial-gradient(circle at 50% 40%, var(--photo-b), var(--photo-a));
    box-shadow: 0 2px 6px rgba(0,0,0,0.25);
  }
  .portrait--lead { left: 25px; top: 4px; width: 254px; height: 254px; }
  .portrait--team { left: 281px; top: 55px; width: 200px; height: 200px; }
  .portrait--desk { left: 171px; top: 227px; width: 192px; height: 192px; }
</style>
</head>
<body>
<div class="banner">
  <div class="hero-panel"></div>

  <h1 class="headline">Dream, believe and<br>you can be the<br><span class="big">BEST....</span></h1>

  <div class="signup-band">
    <p class="signup-pitch">Get <em>NEWSLETTER</em> for easy steps to be <strong>#1</strong>.</p>
    <div class="signup-field signup-field--name">first name</div>
    <div class="signup-field signup-field--email">email address</div>
    <div class="signup-go">go</div>
  </div>

  <div class="portrait portrait--lead" role="img" aria-label="Photo of a smiling businesswoman in front of colleagues"></div>
  <div class="portrait portrait--team" role="img" aria-label="Photo of a smiling saleswoman with her team"></div>
  <div class="portrait portrait--desk" role="img" aria-label="Photo of a young professional woman resting her chin on her hand"></div>
</div>
</body>
</html>
```